Business Card - connecting 2 souls and beggining the journey of self discovery

Logo on the front
with tag line

On the back list of services and contact details

Seminars
workshops
Coaching
podcasts

Daniel Porthwick
Health & Wellbeing Life Coach
0491 372 815
daniel@wovenpathwellness.example
wovenpathwellness.example

Industry/Entity Type

Life Coaching

Contact Information for Business Card

I like the use of colour from the logo to be used. I'm not a fan of white.

Requirements
Must have
• My tagline: Every step weaves your own path
Nice to have
• Use of colour that is in the mind body soul logo

```html
<!DOCTYPE html>
<html lang="en">
<head>
<meta charset="utf-8">
<title>Woven Path Wellness – Business Card</title>
<link rel="stylesheet" href="https://fonts.googleapis.com/css2?family=Lato:wght@400;700&display=swap">
<style>
  :root {
    --purple: #7f3fc2;
    --green: #9cc83c;
    --grey: #77777a;
    --ink: #1f1f22;
    --white: #ffffff;
    --backdrop: #2f2f31;
    --mark: #e9a23b;
  }
  * { box-sizing: border-box; margin: 0; padding: 0; }
  html, body { width: 1200px; height: 900px; overflow: hidden; }
  body {
    background: var(--backdrop);
    font-family: "Lato", Arial, sans-serif;
    position: relative;
  }
  .card {
    position: absolute;
    width: 600px;
    height: 343px;
    overflow: hidden;
    box-shadow: 0 12px 30px rgba(0,0,0,.45);
  }

  /* Front */
  .card--front { left: 540px; top: 70px; background: var(--purple); color: var(--white); text-align: center; }
  .front__mark {
    width: 78px; height: 78px; border-radius: 50%;
    background: var(--mark);
    margin: 52px auto 14px;
  }
  .front__name { font-size: 38px; font-weight: 700; letter-spacing: -0.5px; }
  .front__services { font-size: 17px; margin-top: 22px; letter-spacing: .5px; }
  .front__tagline { font-size: 17px; margin-top: 8px; letter-spacing: 2px; text-transform: uppercase; }

  /* Back */
  .card--back { left: 60px; top: 460px; background: var(--white); }
  .back__brand { position: absolute; left: 34px; top: 32px; display: flex; align-items: center; gap: 14px; }
  .back__mark { width: 56px; height: 56px; border-radius: 50%; background: var(--mark); }
  .back__name { font-size: 28px; font-weight: 700; color: var(--grey); letter-spacing: -0.3px; }
  .back__rule { position: absolute; left: 34px; right: 34px; top: 112px; height: 2px; background: var(--green); }
  .back__phone { position: absolute; left: 34px; top: 132px; font-size: 17px; color: var(--ink); display: flex; align-items: center; gap: 10px; }
  .back__person { position: absolute; right: 34px; top: 128px; text-align right; text-align: right; }
  .person__name { font-size: 27px; font-weight: 700; color: var(--purple); }
  .person__role { font-size: 17px; color: var(--ink); margin-top: 2px; }
  .back__email { position: absolute; right: 34px; top: 212px; font-size: 17px; color: var(--ink); display: flex; align-items: center; gap: 10px; }
  .back__band { position: absolute; left: 0; bottom: 0; width: 600px; height: 110px; }
  .back__web { position: absolute; right: 34px; bottom: 10px; font-size: 18px; color: var(--white); }
  .icon { width: 16px; height: 16px; fill: var(--purple); }
</style>
</head>
<body>

  <section class="card card--front">
    <div class="front__mark"></div>
    <h1 class="front__name">Woven Path Wellness</h1>
    <p class="front__services">Seminars • Workshops • Coaching • Podcasts</p>
    <p class="front__tagline">Every step weaves your own path</p>
  </section>

  <section class="card card--back">
    <div class="back__brand">
      <div class="back__mark"></div>
      <span class="back__name">Woven Path Wellness</span>
    </div>
    <div class="back__rule"></div>

    <p class="back__phone">
      <svg class="icon" viewBox="0 0 16 16" aria-hidden="true"><path d="M4 1c1 0 2 3 2 4s-1 1.5-1 2c.5 1.5 2 3 3.5 3.5.5 0 1-1 2-1s4 1 4 2-1.5 3-3 3C6 14 2 10 1 4.5 1 3 2.5 1 4 1z"/></svg>
      0491 372 815
    </p>

    <div class="back__person">
      <p class="person__name">Daniel Porthwick</p>
      <p class="person__role">Health &amp; Wellbeing Life Coach</p>
    </div>

    <p class="back__email">
      <svg class="icon" viewBox="0 0 16 16" aria-hidden="true"><rect x="1" y="3" width="14" height="10" fill="var(--purple)"/><path d="M1.5 3.5 L8 9 L14.5 3.5" fill="none" stroke="#fff" stroke-width="1.2"/></svg>
      daniel@wovenpathwellness.example
    </p>

    <svg class="back__band" viewBox="0 0 600 110" preserveAspectRatio="none" aria-hidden="true">
      <path d="M0 0 C150 18 300 38 460 52 C300 40 150 26 0 18 Z" fill="var(--green)"/>
      <path d="M0 30 C200 58 380 60 600 62 L600 110 L0 110 Z" fill="var(--purple)"/>
    </svg>
    <p class="back__web">www.wovenpathwellness.example</p>
  </section>

</body>
</html>
```